Business Card Design

We need a business card designed for our new company. Prefer a black card with white logo & writing.

Contact Information for Business Card

Dale Pickett, address: 7-4417 Larchmere Avenue, Abbotsford, BC, V3K 2R9, Office Phone: 604-555-0172, Cell: 604-555-0138, Email: dale@kelsoncoatworks.ca

Colors

Designer to choose only greyscale colors for use in the design.

```html
<!DOCTYPE html>
<html lang="en">
<head>
<meta charset="utf-8">
<title>Kelson Coatworks – Business Card</title>
<link href="https://fonts.googleapis.com/css2?family=Montserrat:wght@400;700;800&display=swap" rel="stylesheet">
<style>
  :root {
    --backdrop: #d9d9d9;
    --card-black: #0f0f0f;
    --ink-white: #ffffff;
    --ink-soft: #e6e6e6;
    --grey-light: #bdbdbd;
    --grey-mid: #7a7a7a;
    --grey-dark: #3a3a3a;
  }
  * { box-sizing: border-box; margin: 0; padding: 0; }
  html, body {
    width: 1200px;
    height: 786px;
    overflow: hidden;
  }
  body {
    background: var(--backdrop);
    font-family: "Montserrat", Arial, sans-serif;
    display: flex;
    align-items: center;
    justify-content: center;
    gap: 40px;
  }
  .card {
    width: 540px;
    height: 309px;
    background: var(--card-black);
    border-radius: 4px;
    position: relative;
    overflow: hidden;
    box-shadow: 0 10px 26px rgba(0,0,0,0.28);
  }

  /* Front */
  .card-front .details {
    position: absolute;
    left: 30px;
    top: 34px;
    color: var(--ink-white);
  }
  .brand {
    display: flex;
    align-items: center;
    gap: 9px;
    font-weight: 800;
    font-size: 19px;
    letter-spacing: 0.5px;
    text-transform: uppercase;
    line-height: 1;
  }
  .brand-mark {
    width: 14px;
    height: 14px;
    border-radius: 50%;
    background: var(--ink-white);
    flex: none;
  }
  .holder-name {
    margin-top: 34px;
    font-weight: 700;
    font-size: 23px;
    line-height: 1;
  }
  .address {
    margin-top: 16px;
    font-size: 13.5px;
    line-height: 1.45;
    color: var(--ink-soft);
  }
  .contact-list {
    list-style: none;
    margin-top: 12px;
    font-size: 13.5px;
    line-height: 1.55;
    color: var(--ink-soft);
  }
  .contact-list li {
    display: flex;
    align-items: center;
    gap: 8px;
  }
  .contact-list svg {
    width: 11px;
    height: 11px;
    fill: var(--ink-soft);
    flex: none;
  }
  .emblem {
    position: absolute;
    left: 270px;
    top: 30px;
    width: 250px;
    height: 250px;
    border-radius: 50%;
    background: var(--ink-white);
    display: flex;
    align-items: center;
    justify-content: center;
  }
  .emblem-art {
    width: 180px;
    height: 150px;
    background: linear-gradient(180deg, #f4f4f4 0%, var(--grey-light) 45%, var(--grey-mid) 100%);
    border-radius: 6px;
  }

  /* Back */
  .card-back .pattern {
    position: absolute;
    inset: 0;
    background: linear-gradient(100deg, #8f8f8f 0%, #4a4a4a 35%, #1a1a1a 65%, #050505 100%);
  }
</style>
</head>
<body>
  <section class="card card-front" aria-label="Business card front">
    <div class="details">
      <div class="brand"><span class="brand-mark"></span>Kelson Coatworks</div>
      <h1 class="holder-name">Dale Pickett</h1>
      <p class="address">7-4417 Larchmere Avenue,<br>Abbotsford, BC, V3K 2R9</p>
      <ul class="contact-list">
        <li>
          <svg viewBox="0 0 24 24" aria-hidden="true"><path d="M6.6 10.8a15.1 15.1 0 0 0 6.6 6.6l2.2-2.2c.3-.3.7-.4 1-.2 1.1.4 2.3.6 3.6.6.6 0 1 .4 1 1V20c0 .6-.4 1-1 1A17 17 0 0 1 3 4c0-.6.4-1 1-1h3.5c.6 0 1 .4 1 1 0 1.3.2 2.5.6 3.6.1.3 0 .7-.2 1z"/></svg>
          604-555-0172
        </li>
        <li>
          <svg viewBox="0 0 24 24" aria-hidden="true"><path d="M7 1h10a2 2 0 0 1 2 2v18a2 2 0 0 1-2 2H7a2 2 0 0 1-2-2V3a2 2 0 0 1 2-2zm0 3v14h10V4zm5 15.5a1.2 1.2 0 1 0 0 2.4 1.2 1.2 0 0 0 0-2.4z"/></svg>
          604-555-0138
        </li>
        <li>
          <svg viewBox="0 0 24 24" aria-hidden="true"><path d="M2 5h20v14H2zm2 2v.5l8 5 8-5V7zm0 2.9V17h16V9.9l-8 5z"/></svg>
          dale@kelsoncoatworks.ca
        </li>
      </ul>
    </div>
    <div class="emblem">
      <div class="emblem-art" role="img" aria-label="Illustration of three stacked coating layers in white, light grey and dark grey"></div>
    </div>
  </section>

  <section class="card card-back" aria-label="Business card back">
    <div class="pattern" role="img" aria-label="Grid of glossy circular brand emblems fading from grey to black"></div>
  </section>
</body>
</html>
```